I need a website, primarily a landing page, for my company, Corvane Group. A sales training and cons

I need a web design/landing page for a new sales training and consulting company, corvane group. We perform "sales experiments" aimed at each individual or team, where we assist in helping them identify their strengths, through a series of "sales experiments" that we can tailor based on the individual and what they're trying to accomplish.

```html
<!DOCTYPE html>
<html lang="en">
<head>
<meta charset="utf-8">
<title>Corvane Group — Sales Experiments</title>
<link rel="stylesheet" href="https://fonts.googleapis.com/css2?family=Open+Sans:wght@300;400;600&family=Poppins:wght@600;700&display=swap">
<style>
  :root {
    --blue: #2a78b8;
    --blue-light: #3f8fd0;
    --ink: #2b2b2b;
    --grey-text: #7a7a7a;
    --heading-grey: #8c8c8c;
    --hero-dark: #141618;
    --white: #ffffff;
    --rule: #eeeeee;
  }
  * { margin: 0; padding: 0; box-sizing: border-box; }
  html, body { width: 800px; height: 1200px; overflow: hidden; background: var(--white); }
  body { position: relative; font-family: "Open Sans", sans-serif; color: var(--ink); }

  /* Hero */
  .hero { position: absolute; left: 154px; top: 35px; width: 484px; height: 306px; }
  .hero-backdrop {
    position: absolute; inset: 0;
    background: radial-gradient(ellipse at 52% 48%, #26313d 0%, #1b1e22 45%, var(--hero-dark) 100%);
  }
  .nav { position: absolute; top: 14px; left: 0; width: 100%; font-size: 7px; color: var(--white); }
  .nav a { position: absolute; color: var(--white); text-decoration: none; white-space: nowrap; }
  .nav a.is-active { color: var(--blue-light); }
  .nav-brand {
    position: absolute; left: 200px; top: 3px; width: 84px;
    display: flex; align-items: center; justify-content: center; gap: 4px;
    font-size: 7px; font-weight: 600; color: var(--white); white-space: nowrap;
  }
  .nav-brand-dot { width: 6px; height: 6px; border-radius: 50%; background: var(--blue); }
  .hero-tagline {
    position: absolute; top: 106px; width: 100%; text-align: center;
    font-weight: 300; font-size: 12px; color: #d8d8d8;
  }
  .hero-title {
    position: absolute; top: 139px; width: 100%; text-align: center;
    font-family: "Poppins", sans-serif; font-weight: 700; font-size: 19px;
    letter-spacing: .5px; color: var(--blue-light); line-height: 24px;
  }
  .hero-sub {
    position: absolute; top: 167px; width: 100%; text-align: center;
    font-size: 7px; color: #e4e4e4;
  }
  .btn {
    position: absolute; height: 19px; border-radius: 10px; font-size: 6.5px;
    display: flex; align-items: center; justify-content: center; color: var(--white);
  }
  .btn-primary { left: 169px; top: 186px; width: 76px; background: var(--blue); }
  .btn-outline { left: 253px; top: 186px; width: 67px; border: 1px solid var(--white); }

  /* About company */
  .section-title {
    position: absolute; top: 355px; left: 0; width: 800px; text-align: center;
    font-family: "Poppins", sans-serif; font-weight: 600; font-size: 16px; color: var(--heading-grey);
  }
  .section-title strong { color: var(--blue); font-weight: 700; }
  .section-underline { position: absolute; top: 377px; left: 375px; width: 50px; height: 1px; background: var(--blue); }
  .section-lead { position: absolute; top: 381px; width: 800px; text-align: center; font-size: 6.5px; color: #555; }
  .about-text {
    position: absolute; left: 179px; top: 420px; width: 204px;
    font-size: 6.7px; line-height: 11.4px; color: var(--grey-text);
  }
  .about-visual {
    position: absolute; left: 405px; top: 419px; width: 210px; height: 168px;
    background: radial-gradient(circle at 50% 50%, #1e5fa8 0%, #0b2a57 25%, #000 65%);
    border: 1px solid #333;
  }
  .rule { position: absolute; left: 154px; top: 598px; width: 462px; height: 1px; background: var(--rule); }

  /* Features */
  .feature { position: absolute; width: 120px; }
  .feature-head { display: flex; align-items: flex-end; gap: 6px; height: 20px; }
  .feature-head svg { width: 18px; height: 20px; flex: none; }
  .feature-title { font-size: 10.5px; color: #333; line-height: 12px; }
  .feature-text { margin-top: 5px; font-size: 6.7px; line-height: 12.8px; color: var(--grey-text); }

  /* About me */
  .about-me { position: absolute; left: 158px; top: 838px; width: 468px; height: 232px; }
  .about-me-backdrop {
    position: absolute; inset: 0;
    background: linear-gradient(100deg, #3a3a3a 0%, #2c2c2c 45%, #1f1f1f 100%);
  }
  .about-me-title {
    position: absolute; left: 60px; top: 40px; width: 130px; text-align: center;
    font-family: "Poppins", sans-serif; font-weight: 600; font-size: 16px; color: #cfcfcf;
  }
  .about-me-title span { color: var(--blue-light); }
  .about-me-text {
    position: absolute; left: 19px; top: 64px; width: 216px;
    font-size: 6.6px; line-height: 11.7px; color: #ececec;
  }
  .btn-read { left: 20px; top: 151px; width: 58px; height: 19px; border: 1px solid var(--white); font-size: 6.5px; }
  .brand-card {
    position: absolute; left: 246px; top: 39px; width: 213px; height: 156px;
    background: var(--white); border-radius: 9px;
    display: flex; align-items: center; justify-content: center; gap: 8px;
  }
  .brand-dot { width: 14px; height: 14px; border-radius: 50%; background: var(--blue); }
  .brand-name { font-weight: 600; font-size: 18px; color: var(--blue); }
</style>
</head>
<body>

<header class="hero">
  <div class="hero-backdrop" role="img" aria-label="Dark hero backdrop with a large blue and grey double helix graphic"></div>
  <nav class="nav">
    <a class="is-active" style="left:27px;top:4px">Home</a>
    <a style="left:66px;top:4px">About Corvane Group</a>
    <a style="left:149px;top:4px">About me</a>
    <span class="nav-brand"><span class="nav-brand-dot" aria-hidden="true"></span>Corvane Group</span>
    <a style="left:345px;top:4px">Experiments</a>
    <a style="left:405px;top:4px">Blog</a>
    <a style="left:438px;top:4px">Contact</a>
  </nav>
  <p class="hero-tagline">Success. It's in your DNA</p>
  <h1 class="hero-title">CORVANE GROUP</h1>
  <p class="hero-sub">Will Help You To Find</p>
  <a class="btn btn-primary">Know About Us</a>
  <a class="btn btn-outline">Get In Touch</a>
</header>

<h2 class="section-title">About <strong>Corvane Group</strong></h2>
<div class="section-underline"></div>
<p class="section-lead">Lorem ipsum dolor sit amet, consectetur adipiscing elit.</p>

<p class="about-text">Lorem ipsum dolor sit amet, consectetur adipiscing elit, sed do eiusmod tempor incididunt ut labore et dolore magna aliqua. Ut enim ad minim veniam, quis nostrud exercitation ullamco laboris nisi ut aliquip ex ea commodo consequat. Lorem ipsum dolor sit amet, consectetur adipiscing elit, sed do eiusmod tempor incididunt ut labore et dolore magna aliqua. Ut enim ad minim veniam, quis nostrud exercitation ullamco laboris nisi ut aliquip ex ea commodo consequat. Lorem ipsum dolor sit amet, consectetur adipiscing elit, sed do eiusmod tempor incididunt ut labore et dolore magna aliqua. Ut enim ad minim veniam, quis nostrud exercitation ullamco laboris nisi ut aliquip ex ea commodo consequat.</p>
<div class="about-visual" role="img" aria-label="Glowing blue molecule illustration on black"></div>
<div class="rule"></div>

<section class="features">
  <div class="feature" style="left:185px;top:628px">
    <div class="feature-head">
      <svg viewBox="0 0 18 20" fill="none" stroke="#2a78b8" stroke-width="1"><path d="M2 17 L14 3 L16 5 L4 19 Z"/><path d="M3 3 L16 17"/><path d="M2 5 L5 2"/></svg>
      <span class="feature-title">Feature One</span>
    </div>
    <p class="feature-text">Lorem ipsum dolor sit amet, consectetur adipiscing elit, sed do eiusmod tempor incididunt ut labore et dolore.</p>
  </div>
  <div class="feature" style="left:329px;top:628px">
    <div class="feature-head">
      <svg viewBox="0 0 18 20" fill="none" stroke="#2a78b8" stroke-width="1"><path d="M9 2 C4 2 2 6 4 9 C5 11 7 12 7 14 H11 C11 12 13 11 14 9 C16 6 14 2 9 2 Z"/><path d="M7 16 H11 M8 18 H10"/></svg>
      <span class="feature-title">Feature two</span>
    </div>
    <p class="feature-text">Lorem ipsum dolor sit amet, consectetur adipiscing elit, sed do eiusmod tempor incididunt ut labore et dolore.</p>
  </div>
  <div class="feature" style="left:473px;top:628px">
    <div class="feature-head">
      <svg viewBox="0 0 18 20" fill="none" stroke="#2a78b8" stroke-width="1"><path d="M9 3 L17 7 L9 11 L1 7 Z"/><path d="M1 10 L9 14 L17 10"/><path d="M1 13 L9 17 L17 13"/></svg>
      <span class="feature-title">Feature three</span>
    </div>
    <p class="feature-text">Lorem ipsum dolor sit amet, consectetur adipiscing elit, sed do eiusmod tempor incididunt ut labore et dolore.</p>
  </div>
  <div class="feature" style="left:185px;top:748px">
    <div class="feature-head">
      <svg viewBox="0 0 18 20" fill="none" stroke="#2a78b8" stroke-width="1"><path d="M9 3 L17 7 L9 11 L1 7 Z"/><path d="M1 10 L9 14 L17 10"/><path d="M1 13 L9 17 L17 13"/></svg>
      <span class="feature-title">Feature four</span>
    </div>
    <p class="feature-text">Lorem ipsum dolor sit amet, consectetur adipiscing elit, sed do eiusmod tempor incididunt ut labore et dolore.</p>
  </div>
  <div class="feature" style="left:329px;top:748px">
    <div class="feature-head">
      <svg viewBox="0 0 18 20" fill="none" stroke="#2a78b8" stroke-width="1"><path d="M3 3 L15 15 L16 19 L12 18 L0 6 Z"/><path d="M2 19 H17"/></svg>
      <span class="feature-title">Feature five</span>
    </div>
    <p class="feature-text">Lorem ipsum dolor sit amet, consectetur adipiscing elit, sed do eiusmod tempor incididunt ut labore et dolore.</p>
  </div>
  <div class="feature" style="left:473px;top:748px">
    <div class="feature-head">
      <svg viewBox="0 0 18 20" fill="none" stroke="#2a78b8" stroke-width="1"><circle cx="9" cy="3" r="1.6"/><path d="M9 5 V18"/><path d="M5 8 H13"/><path d="M2 12 C3 16 6 18 9 18 C12 18 15 16 16 12"/></svg>
      <span class="feature-title">Feature six</span>
    </div>
    <p class="feature-text">Lorem ipsum dolor sit amet, consectetur adipiscing elit, sed do eiusmod tempor incididunt ut labore et dolore.</p>
  </div>
</section>

<section class="about-me">
  <div class="about-me-backdrop" role="img" aria-label="Darkened photo of business people shaking hands in an office"></div>
  <h2 class="about-me-title">About<span>Me</span></h2>
  <p class="about-me-text">Lorem ipsum dolor sit amet, consectetur adipiscing elit, sed do eiusmod tempor incididunt ut labore et dolore magna aliqua. Ut enim ad minim veniam, quis nostrud exercitation ullamco laboris nisi ut aliquip. Lorem ipsum dolor sit amet, consectetur adipiscing elit, sed do eiusmod tempor incididunt ut labore et dolore magna aliqua. Ut enim ad minim veniam, quis nostrud exercitation ullamco laboris nisi ut aliquip.</p>
  <a class="btn btn-read">Read More</a>
  <div class="brand-card">
    <span class="brand-dot" aria-hidden="true"></span>
    <span class="brand-name">Corvane Group</span>
  </div>
</section>

</body>
</html>
```